Report template for evaluation reports to be used by non designers

We are looking for a report template that meets all the requirements listed in the attached documents. letter head, logo etc have been enclosed. Its important that the colour integrity is kept, but beyond that options are welcome.
Its important that the document is extremely easy to use and that is able to be adapted to include eatables, figures, pictures, text boxes etc and keep the integrity of the template

Target Market(s)

Governments, Civil society organisations and research institutions

Font styles to use
Sans Serif

Colors
6b449b
876aae
c0c0c0
000000

Requirements
Must have
• Clean, professional, not concluded, modern, must be easy to use
Should not have
• too busy, hard to use

```html
<!DOCTYPE html>
<html lang="en">
<head>
<meta charset="utf-8">
<title>Meridian Research Institute – Report Template</title>
<link href="https://fonts.googleapis.com/css2?family=Montserrat:wght@400;500;600;700;800&display=swap" rel="stylesheet">
<style>
  :root{
    --purple:#6b449b;
    --purple-soft:#55408a;
    --lilac:#876aae;
    --silver:#c0c0c0;
    --paper:#f7f7f5;
    --ink:#1a1a1a;
    --stage:#0b0c0e;
    --grey-wedge:#dcdcde;
  }
  *{box-sizing:border-box;margin:0;padding:0}
  html,body{width:1200px;height:1066px;overflow:hidden;background:var(--stage)}
  body{font-family:"Montserrat",Arial,sans-serif;position:relative}
  .sheet{position:absolute;width:297px;height:420px;overflow:hidden;background:var(--paper)}
  .sheet--purple{background:var(--purple-soft)}

  .brand{position:absolute;text-align:center;color:var(--ink);font-weight:500;line-height:1}
  .brand__name{display:block;font-size:17px;letter-spacing:4px}
  .brand__sub{display:block;font-size:4px;letter-spacing:1.6px;margin-top:4px}
  .brand--light{color:#fff}

  .contact{position:absolute;left:0;right:0;display:flex;align-items:center;font-size:3.4px;color:#333;gap:3px}
  .contact__item{display:flex;align-items:center;gap:2px}
  .contact__icon{width:5px;height:5px;border-radius:50%;border:0.6px solid #444;display:inline-block}
  .sheet--purple .contact{color:#fff;justify-content:center}
  .sheet--purple .contact__icon{border-color:#fff}

  .regtab{position:absolute;right:0;height:10px;width:110px;background:#1b1b1b;color:#eee;font-size:3.6px;
    display:flex;align-items:center;justify-content:center;clip-path:polygon(8% 0,100% 0,100% 100%,0 100%)}
  .servicebar{position:absolute;left:0;right:0;bottom:0;height:11px;background:var(--purple);color:#fff;
    font-size:3.8px;font-weight:700;display:flex;align-items:center;justify-content:center;border-top:1.5px solid var(--silver)}
  .servicebar--plain{background:none;border:none;height:auto}

  /* cover */
  .cover .brand{left:0;right:0;top:184px}
  .cover .brand__name{font-size:24px;letter-spacing:5px}
  .cover .brand__sub{font-size:5.4px;letter-spacing:2.4px;margin-top:6px}
  .cover .contact{top:468px}
  .reg-line{position:absolute;left:0;right:0;text-align:center;color:#fff;font-size:3.6px}

  /* title page */
  .title-page .brand{left:26px;top:22px;color:#fff;text-align:left}
  .wedge{position:absolute;inset:0}
  .report-title{position:absolute;left:26px;top:355px;color:#fff;font-size:12px;font-weight:600;line-height:1.15}
  .report-author{position:absolute;right:16px;top:385px;text-align:right}
  .report-author__name{color:var(--purple);font-size:9.5px;font-weight:700;display:block}
  .report-author__date{color:#333;font-size:5.4px;display:block;margin-top:3px}

  /* letterhead */
  .letterhead .brand{left:26px;top:22px;text-align:left}

  /* index */
  .index .brand{right:28px;top:22px;text-align:left}
  .index__title{position:absolute;left:28px;top:63px;color:var(--purple);font-size:12.5px;font-weight:800}
  .index__rule{position:absolute;left:28px;width:241px;top:84px;height:1.2px;background:#888}
  .toc{position:absolute;left:28px;top:89px;width:241px;font-size:3.8px;color:#333}
  .toc__row{display:flex;height:15.2px;align-items:center;border-bottom:0.9px solid var(--lilac)}
  .toc__row--head{height:11px}
  .toc__no{width:26px;padding-left:2px}
  .toc__no--num{text-align:right;padding-right:6px;padding-left:0;width:14px;margin-right:12px}
  .toc__topic{flex:1;padding-left:2px}
  .toc__page{width:38px;padding-left:14px}
  .toc__rule-v{position:absolute;top:95px;width:0.8px;height:283px;background:#bbb}

  /* memo */
  .memo .brand{right:26px;top:22px;text-align:left}
  .memo__to{position:absolute;left:17px;top:35px}
  .memo__name{color:var(--purple);font-size:6.5px;font-weight:700;display:block}
  .memo__date{font-size:2.8px;color:#333;display:block;margin-top:2px}
  .memo__rule{position:absolute;left:17px;width:280px;top:55px;height:0.8px;background:var(--lilac)}
  .memo__disc-rule{position:absolute;left:17px;width:280px;top:354px;height:0.6px;background:#999}
  .disclaimer{position:absolute;left:17px;right:17px;top:357px;font-size:2.8px;color:#333;line-height:1.35}
  .disclaimer__head{color:var(--purple);font-weight:700;display:block}
</style>
</head>
<body>

<!-- Cover -->
<section class="sheet sheet--purple cover" style="left:138px;top:94px">
  <div class="brand brand--light"><span class="brand__name">MERIDIAN</span><span class="brand__sub">RESEARCH INSTITUTE</span></div>
  <div class="contact">
    <span class="contact__item"><i class="contact__icon"></i>+41 00 000 00 00</span>
    <span class="contact__item"><i class="contact__icon"></i>info@meridianinstitute.org</span>
    <span class="contact__item"><i class="contact__icon"></i>www.meridianinstitute.org</span>
  </div>
  <p class="reg-line" style="top:478px">Registration Number: REG-000.000.000</p>
  <div class="servicebar servicebar--plain" style="top:404px;display:flex">Evaluation &nbsp;|&nbsp; Research &nbsp;|&nbsp; Policy Analysis &nbsp;|&nbsp; Capacity Development &nbsp;|&nbsp; Training</div>
</section>

<!-- Title page -->
<section class="sheet sheet--purple title-page" style="left:457px;top:94px">
  <div class="brand"><span class="brand__name">MERIDIAN</span><span class="brand__sub">RESEARCH INSTITUTE</span></div>
  <svg class="wedge" viewBox="0 0 297 420" aria-hidden="true"><polygon points="0,420 297,356 297,420" fill="var(--grey-wedge)"/></svg>
  <h1 class="report-title">Name of<br>the report</h1>
  <p class="report-author"><span class="report-author__name">Daniel Hart</span><span class="report-author__date">on 27th June 2018</span></p>
</section>

<!-- Letterhead -->
<section class="sheet letterhead" style="left:770px;top:94px">
  <div class="brand"><span class="brand__name">MERIDIAN</span><span class="brand__sub">RESEARCH INSTITUTE</span></div>
  <div class="contact" style="top:398px;left:16px">
    <span class="contact__item"><i class="contact__icon"></i>+41 00 000 00 00</span>
    <span class="contact__item"><i class="contact__icon"></i>info@meridianinstitute.org</span>
    <span class="contact__item"><i class="contact__icon"></i>www.meridianinstitute.org</span>
  </div>
  <div class="regtab" style="top:396px">Registration Number: REG-000.000.000</div>
  <div class="servicebar">Evaluation &nbsp;|&nbsp; Research &nbsp;|&nbsp; Policy Analysis &nbsp;|&nbsp; Capacity Development &nbsp;|&nbsp; Training</div>
</section>

<!-- Index page -->
<section class="sheet index" style="left:131px;top:546px">
  <div class="brand"><span class="brand__name">MERIDIAN</span><span class="brand__sub">RESEARCH INSTITUTE</span></div>
  <h2 class="index__title">EXAMPLE OF INDEX</h2>
  <div class="index__rule"></div>
  <div class="toc__rule-v" style="left:54px"></div>
  <div class="toc__rule-v" style="left:230px"></div>
  <div class="toc">
    <div class="toc__row toc__row--head"><span class="toc__no">S.No.</span><span class="toc__topic">TOPIC</span><span class="toc__page" style="padding-left:8px">Page No.</span></div>
    <div class="toc__row"><span class="toc__no toc__no--num">1)</span><span class="toc__topic">LOREM IPSUM</span><span class="toc__page">1</span></div>
    <div class="toc__row"><span class="toc__no toc__no--num">2)</span><span class="toc__topic">LOREM IPSUM</span><span class="toc__page">2</span></div>
    <div class="toc__row"><span class="toc__no toc__no--num">3)</span><span class="toc__topic">LOREM IPSUM</span><span class="toc__page">3</span></div>
    <div class="toc__row"><span class="toc__no toc__no--num">4)</span><span class="toc__topic">LOREM IPSUM</span><span class="toc__page">4</span></div>
    <div class="toc__row"><span class="toc__no toc__no--num">5)</span><span class="toc__topic">LOREM IPSUM</span><span class="toc__page">5</span></div>
    <div class="toc__row"><span class="toc__no toc__no--num">6)</span><span class="toc__topic">LOREM IPSUM</span><span class="toc__page">6</span></div>
    <div class="toc__row"><span class="toc__no toc__no--num">7)</span><span class="toc__topic">LOREM IPSUM</span><span class="toc__page">7</span></div>
    <div class="toc__row"><span class="toc__no toc__no--num">8)</span><span class="toc__topic">LOREM IPSUM</span><span class="toc__page">8</span></div>
    <div class="toc__row"><span class="toc__no toc__no--num">9)</span><span class="toc__topic">LOREM IPSUM</span><span class="toc__page">9</span></div>
    <div class="toc__row"><span class="toc__no toc__no--num">10)</span><span class="toc__topic">LOREM IPSUM</span><span class="toc__page">10</span></div>
    <div class="toc__row"><span class="toc__no toc__no--num">11)</span><span class="toc__topic">LOREM IPSUM</span><span class="toc__page">11</span></div>
    <div class="toc__row"><span class="toc__no toc__no--num">12)</span><span class="toc__topic">LOREM IPSUM</span><span class="toc__page">12</span></div>
    <div class="toc__row"><span class="toc__no toc__no--num">13)</span><span class="toc__topic">LOREM IPSUM</span><span class="toc__page">13</span></div>
    <div class="toc__row"><span class="toc__no toc__no--num">14)</span><span class="toc__topic">LOREM IPSUM</span><span class="toc__page">14</span></div>
  </div>
  <div class="contact" style="top:398px;left:16px">
    <span class="contact__item"><i class="contact__icon"></i>+41 00 000 00 00</span>
    <span class="contact__item"><i class="contact__icon"></i>info@meridianinstitute.org</span>
    <span class="contact__item"><i class="contact__icon"></i>www.meridianinstitute.org</span>
  </div>
  <div class="regtab" style="top:396px">Registration Number: REG-000.000.000</div>
  <div class="servicebar">Evaluation &nbsp;|&nbsp; Research &nbsp;|&nbsp; Policy Analysis &nbsp;|&nbsp; Capacity Development &nbsp;|&nbsp; Training</div>
</section>

<!-- Memo page -->
<section class="sheet memo" style="left:451px;top:551px">
  <div class="brand"><span class="brand__name">MERIDIAN</span><span class="brand__sub">RESEARCH INSTITUTE</span></div>
  <p class="memo__to"><span class="memo__name">Lena Varga</span><span class="memo__date">22nd June 2018</span></p>
  <div class="memo__rule" style="width:263px"></div>
  <div class="memo__disc-rule" style="width:263px"></div>
  <p class="disclaimer"><span class="disclaimer__head">DISCLAIMER</span>The views expressed in this report are those of the authors and do not necessarily reflect the position of the institute or its partners. Content may be reproduced for non-commercial purposes provided the source is acknowledged. All data were accurate at the time of publication and are subject to revision.</p>
  <div class="contact" style="top:398px;left:16px">
    <span class="contact__item"><i class="contact__icon"></i>+41 00 000 00 00</span>
    <span class="contact__item"><i class="contact__icon"></i>info@meridianinstitute.org</span>
    <span class="contact__item"><i class="contact__icon"></i>www.meridianinstitute.org</span>
  </div>
  <div class="regtab" style="top:396px">Registration Number: REG-000.000.000</div>
  <div class="servicebar">Evaluation &nbsp;|&nbsp; Research &nbsp;|&nbsp; Policy Analysis &nbsp;|&nbsp; Capacity Development &nbsp;|&nbsp; Training</div>
</section>

</body>
</html>
```